Business card design needed

Double sided
Color, unique, elegant

Maybe put this quote somewhere?? But I think it might make it to cluttered?
“The Pilates Method of Body
Conditioning develops the body
uniformly, corrects posture, restores
vitality, invigorates the mind and
elevates the spirit”
- Lionel Hartwick

Industry/Entity Type

Business

Contact Information for Business Card

Marla Trevisick
Pilates Instructor & Personal trainer
Mobile: 0498260543
www.kovira.com.au
email: koviraheal.motion@brintmail.com

```html
<!DOCTYPE html>
<html lang="en">
<head>
<meta charset="utf-8">
<title>Kovira Health and Fitness – Business Card</title>
<link rel="stylesheet" href="https://fonts.googleapis.com/css2?family=Questrial&family=Poiret+One&display=swap">
<style>
  :root {
    --bg: #e9e9e7;
    --card-green: #8fbd5c;
    --card-white: #ffffff;
    --ink-grey: #555a55;
    --ink-dark: #3e423e;
    --accent-green: #8cc04a;
    --accent-pink: #c46aa8;
    --quote-white: #f4f8ee;
  }
  * { margin: 0; padding: 0; box-sizing: border-box; }
  html, body {
    width: 1200px; height: 900px; overflow: hidden;
    background: var(--bg);
    font-family: "Questrial", "Century Gothic", sans-serif;
  }
  .canvas {
    width: 1200px; height: 900px;
    display: flex; flex-direction: column;
    align-items: center; justify-content: center; gap: 60px;
  }
  .card {
    width: 560px; height: 340px;
    position: relative;
    box-shadow: 0 6px 18px rgba(0,0,0,0.15);
  }
  .card--back { background: var(--card-green); }
  .card--front { background: var(--card-white); }

  .brand { position: absolute; display: flex; flex-direction: column; }
  .brand__row { display: flex; align-items: center; gap: 12px; }
  .brand__dot {
    width: 18px; height: 18px; border-radius: 50%;
    background: var(--accent-pink);
  }
  .brand__name {
    font-family: "Questrial", sans-serif;
    font-size: 40px; letter-spacing: 4px;
    color: var(--ink-grey); text-transform: uppercase;
  }
  .brand__tagline {
    font-size: 16px; color: var(--ink-dark); margin-top: 4px;
  }
  .card--back .brand { left: 44px; top: 150px; }
  .card--front .brand { left: 44px; top: 60px; }

  .quote {
    position: absolute; right: 36px; top: 150px; width: 250px;
    color: var(--quote-white); font-size: 12.5px; line-height: 1.4;
  }
  .quote__author {
    display: block; text-align: right; margin-top: 10px;
    font-weight: bold; font-size: 12.5px;
  }

  .contact {
    position: absolute; right: 40px; top: 160px;
    text-align: right; color: var(--ink-dark);
  }
  .contact__name { font-size: 22px; color: var(--accent-green); letter-spacing: 0.5px; }
  .contact__role { font-size: 15px; margin-top: 2px; }
  .contact__list { list-style: none; margin-top: 16px; font-size: 15px; line-height: 1.5; }
  .contact__label { color: var(--accent-green); margin-right: 4px; }
</style>
</head>
<body>
<main class="canvas">
  <section class="card card--back" aria-label="Card back">
    <div class="brand">
      <div class="brand__row">
        <span class="brand__dot"></span>
        <span class="brand__name">Kovira</span>
      </div>
      <span class="brand__tagline">Health and Fitness</span>
    </div>
    <blockquote class="quote">
      “The Pilates Method of Body Conditioning develops the body uniformly, corrects posture, restores vitality, invigorates the mind and elevates the spirit”
      <cite class="quote__author">- Lionel Hartwick</cite>
    </blockquote>
  </section>

  <section class="card card--front" aria-label="Card front">
    <div class="brand">
      <div class="brand__row">
        <span class="brand__dot"></span>
        <span class="brand__name">Kovira</span>
      </div>
      <span class="brand__tagline">Health and Fitness</span>
    </div>
    <div class="contact">
      <p class="contact__name">Marla Trevisick</p>
      <p class="contact__role">Pilates Instructor &amp; Personal trainer</p>
      <ul class="contact__list">
        <li><span class="contact__label">M:</span>0498 260 543</li>
        <li><span class="contact__label">E:</span>koviraheal.motion@brintmail.com</li>
        <li>www.kovira.com.au</li>
      </ul>
    </div>
  </section>
</main>
</body>
</html>
```